Tolvane Air and Electrical Website

Simple and easy to use website for a Electrical and Air Conditioning contracting business.Use stock photosOnline contact portallogo still to be supplied

Target Market(s)

Mums and Dads who want a local contractor

Coding

Coded - Design and coding required

Number of Pages Required

2 page

Font styles to use
Sans Serif

Colors
f04a50
3276b5
33a6d7

Requirements
Must have
• Simple and easy to use
• Ph number
• 4 web address; linked to page
• 0417385926
• tolvane.com.au
• tolvaneelectrical.com.au
• tolvaneairandelectrical.com.au
• tolvaneair.com.au
Nice to have
• Split System Air Con Picture
• Electrical Pictures

```html
<!DOCTYPE html>
<html lang="en">
<head>
<meta charset="utf-8">
<title>Tolvane Air and Electrical</title>
<link rel="stylesheet" href="https://fonts.googleapis.com/css2?family=Exo+2:wght@500;600;700&family=Open+Sans:wght@400;600;700&display=swap">
<style>
:root{
  --red:#f04a50;
  --blue:#3276b5;
  --sky:#33a6d7;
  --ink:#222;
  --text:#555;
  --dark:#2b2b2b;
  --white:#fff;
}
*{box-sizing:border-box;margin:0;padding:0}
html,body{width:1200px;height:3593px;overflow:hidden}
body{position:relative;background:var(--white);font-family:'Open Sans',sans-serif;color:var(--text)}
.head-font{font-family:'Exo 2',sans-serif}
section,header,footer{position:absolute;left:0;width:1200px}

/* header */
.site-header{top:0;height:120px;background:var(--white)}
.brand{position:absolute;left:60px;top:30px;display:flex;align-items:center;gap:12px}
.brand-mark{width:34px;height:34px;background:var(--red)}
.brand-name{font-family:'Exo 2',sans-serif;font-weight:700;font-size:30px;color:var(--blue);line-height:1}
.call{position:absolute;left:700px;top:22px;font-size:19px;color:var(--red)}
.call strong{color:var(--blue);font-weight:600}
.quote-btn{position:absolute;left:940px;top:18px;width:198px;height:36px;border-radius:18px;background:var(--red);color:#fff;font-family:'Exo 2',sans-serif;font-weight:700;font-size:13px;display:flex;align-items:center;justify-content:center;letter-spacing:.5px}
.main-nav{position:absolute;left:350px;top:79px;height:41px;display:flex}
.main-nav a{width:132px;height:41px;background:var(--blue);color:#fff;text-decoration:none;font-family:'Exo 2',sans-serif;font-weight:700;font-size:13px;display:flex;align-items:center;justify-content:center;transform:skewX(-30deg);border-right:2px solid #fff}
.main-nav a span{transform:skewX(30deg)}
.main-nav a.active{background:var(--red)}

/* hero */
.hero{top:120px;height:718px;background:linear-gradient(180deg,#7a5a48 0%,#8f6b55 40%,#5c4538 75%,#3a3030 100%)}
.hero-photo{position:absolute;inset:0;background:linear-gradient(90deg,#6d4f40,#9a7560 50%,#5a4a44)}
.hero-shade{position:absolute;left:0;top:0;width:100%;height:100%;background:linear-gradient(180deg,rgba(0,0,0,.25),rgba(0,0,0,.1) 40%,rgba(20,20,30,.65) 72%,rgba(20,20,30,.75))}
.hero h1{position:absolute;top:162px;width:100%;text-align:center;color:#fff;font-family:'Exo 2',sans-serif;font-weight:700;font-size:33px;line-height:40px;letter-spacing:.5px}
.btn{display:flex;align-items:center;justify-content:center;color:#fff;font-family:'Exo 2',sans-serif;font-weight:700;font-size:12px;letter-spacing:.5px;position:absolute}
.btn-blue{background:var(--blue)}
.btn-red{background:var(--red)}
.hero .explore{left:511px;top:263px;width:178px;height:43px}
.cat-title{position:absolute;top:506px;width:100%;text-align:center;color:var(--sky);font-family:'Exo 2',sans-serif;font-weight:600;font-size:20px}
.cat-down{position:absolute;top:540px;left:593px}
.categories{position:absolute;top:598px;left:120px;width:960px;display:flex;justify-content:space-between}
.category{width:170px;text-align:center;color:#fff;font-size:15px}
.category svg{display:block;margin:0 auto 14px}
.hero .arrow{position:absolute;top:625px}

/* services */
.services{top:838px;height:642px;background:#fff}
.section-title{position:absolute;width:100%;text-align:center;font-family:'Exo 2',sans-serif;font-weight:700;font-size:30px}
.services .section-title{top:72px;color:var(--blue)}
.service-card{position:absolute;top:144px;width:304px}
.service-card .photo{height:200px}
.service-card h3{margin-top:27px;font-family:'Exo 2',sans-serif;font-weight:600;font-size:17px;color:var(--ink)}
.service-card .rule{margin-top:10px;width:100%;height:1px;background:#ddd}
.service-card ul{list-style:none;margin-top:12px;display:grid;grid-template-columns:1fr 1fr;column-gap:8px;row-gap:4px;font-size:11.5px;color:#666}
.service-card ul.single{grid-template-columns:1fr}
.service-card li::before{content:"» ";color:#999}
.service-card .btn{position:absolute;top:388px;left:0;width:128px;height:30px;font-size:11px}
.services .arrow{position:absolute;top:230px}

/* experience */
.experience{top:1480px;height:496px;background:var(--sky)}
.experience h2{position:absolute;top:88px;width:100%;text-align:center;color:#fff;font-family:'Exo 2',sans-serif;font-weight:700;font-size:28px;line-height:34px}
.experience .photo{position:absolute;left:240px;top:173px;width:263px;height:244px}
.experience .copy{position:absolute;left:546px;top:170px;width:390px;color:#fff;font-size:12.5px;line-height:20px}
.experience .copy p+p{margin-top:20px}
.outline-btn{position:absolute;left:544px;top:381px;width:160px;height:33px;border:1.5px solid #fff;color:#fff;font-family:'Exo 2',sans-serif;font-weight:700;font-size:11px;display:flex;align-items:center;justify-content:center}

/* why */
.why{top:1976px;height:522px;background:#fff}
.why-card{position:absolute;top:79px;width:304px;text-align:center}
.why-card .photo{height:201px}
.why-card h3{margin-top:24px;font-family:'Exo 2',sans-serif;font-weight:600;font-size:17px;color:var(--ink)}
.why-card .rule{width:100px;height:1px;background:#ddd;margin:12px auto 0}
.why-card p{margin:18px auto 0;width:270px;font-size:11.5px;line-height:19px;color:#666}
.why-card .more{display:block;margin-top:14px;font-family:'Exo 2',sans-serif;font-weight:700;font-size:11px;color:var(--blue)}
.why-card .more.hot{color:var(--red)}

/* testimonials */
.testimonials{top:2498px;height:424px;background:linear-gradient(180deg,#4a4340,#3a3432 60%,#2f2a28)}
.testimonials .section-title{top:62px;color:#fff}
.testimonials blockquote{position:absolute;left:170px;top:132px;width:860px;text-align:center;color:#fff;font-size:19px;line-height:29px}
.q{color:var(--red);font-weight:700}
.testimonials .date{position:absolute;top:272px;width:100%;text-align:center;color:var(--red);font-family:'Exo 2',sans-serif;font-weight:600;font-size:12px;letter-spacing:1px}
.testimonials .name{position:absolute;top:305px;width:100%;text-align:center;color:#fff;font-family:'Exo 2',sans-serif;font-weight:700;font-size:14px}
.testimonials .job{position:absolute;top:328px;width:100%;text-align:center;color:#ddd;font-size:12px}
.dots{position:absolute;left:1105px;top:190px;display:flex;flex-direction:column;gap:8px}
.dots i{width:8px;height:8px;border-radius:50%;border:1.5px solid #ccc;display:block}
.dots i.on{background:#fff;border-color:#fff}

/* breakdown */
.breakdown{top:2922px;height:203px;background:var(--red)}
.breakdown h2{position:absolute;left:120px;top:60px;color:#fff;font-family:'Exo 2',sans-serif;font-weight:700;font-size:25px}
.breakdown p{position:absolute;left:120px;top:100px;width:700px;color:#fff;font-size:11.5px;line-height:19px}
.breakdown .btn{left:905px;top:75px;width:174px;height:45px;font-size:12px}

/* footer */
.site-footer{top:3125px;height:468px;background:linear-gradient(180deg,#3e7fbd,var(--blue) 40%,#2d6aa4)}
.site-footer h4{position:absolute;top:72px;color:#fff;font-family:'Exo 2',sans-serif;font-weight:700;font-size:20px}
.field{position:absolute;border:1.5px solid rgba(255,255,255,.6);color:#e8f0f8;font-size:12px;padding:10px 18px}
.send{position:absolute;left:240px;top:345px;width:172px;height:39px;background:var(--red);color:#fff;font-family:'Exo 2',sans-serif;font-weight:700;font-size:11px;display:flex;align-items:center;justify-content:center}
.contact-info{position:absolute;left:719px;top:104px;color:#fff}
.contact-info .tel{font-family:'Exo 2',sans-serif;font-weight:700;font-size:15px}
.contact-info address{margin-top:22px;font-style:normal;font-size:12px;line-height:19px}
.socials{position:absolute;left:719px;top:264px;display:flex;gap:10px}
.socials i{width:14px;height:14px;border:1.5px solid #fff;display:block}
.foot-rule{position:absolute;left:719px;top:324px;width:360px;height:1px;background:rgba(255,255,255,.5)}
.copyright{position:absolute;left:719px;top:346px;color:#fff;font-size:12px;line-height:19px}
</style>
</head>
<body>

<header class="site-header">
  <div class="brand"><span class="brand-mark"></span><span class="brand-name">TOLVANE</span></div>
  <div class="call">Call Us. <strong>0417385926</strong></div>
  <div class="quote-btn">GET A FREE QUOTES</div>
  <nav class="main-nav">
    <a class="active"><span>HOME</span></a>
    <a><span>ABOUT US</span></a>
    <a><span>SERVICES</span></a>
    <a><span>WHY US</span></a>
    <a><span>TESTIMONIALS</span></a>
    <a><span>CONTACT US</span></a>
  </nav>
</header>

<section class="hero">
  <div class="hero-photo" role="img" aria-label="Woman relaxing in an armchair beneath a wall-mounted split system air conditioner against a brick wall"></div>
  <div class="hero-shade"></div>
  <h1>WE PROVIDE ELECTRICAL<br>AND AIR CONDITIONING SERVICES</h1>
  <div class="btn btn-blue explore">EXPLORE MORE</div>
  <div class="cat-title">SERVICE CATEGORIES</div>
  <svg class="cat-down" width="14" height="18" viewBox="0 0 14 18"><path d="M7 1v15M2 11l5 5 5-5" stroke="#33a6d7" stroke-width="1.5" fill="none"/></svg>
  <svg class="arrow" style="left:58px" width="14" height="24" viewBox="0 0 14 24"><path d="M12 2 2 12l10 10" stroke="#fff" stroke-width="2" fill="none"/></svg>
  <svg class="arrow" style="left:1128px" width="14" height="24" viewBox="0 0 14 24"><path d="M2 2l10 10-10 10" stroke="#fff" stroke-width="2" fill="none"/></svg>
  <div class="categories">
    <div class="category">
      <svg width="44" height="40" viewBox="0 0 44 40" fill="none" stroke="#fff" stroke-width="2"><rect x="3" y="4" width="38" height="16" rx="2"/><path d="M8 15h28M12 26v8M22 26v10M32 26v8"/></svg>
      Air Conditioning
    </div>
    <div class="category">
      <svg width="44" height="40" viewBox="0 0 44 40" fill="none" stroke="#fff" stroke-width="2"><circle cx="22" cy="18" r="14"/><path d="M17 32v5h10v-5M24 9l-5 10h6l-5 10"/></svg>
      Electricians
    </div>
    <div class="category">
      <svg width="44" height="40" viewBox="0 0 44 40" fill="none" stroke="#fff" stroke-width="2"><rect x="5" y="4" width="34" height="26" rx="2"/><path d="M5 22h34M12 34h20M14 13h16"/></svg>
      Split System
    </div>
    <div class="category">
      <svg width="44" height="40" viewBox="0 0 44 40" fill="none" stroke="#fff" stroke-width="2"><circle cx="17" cy="20" r="7"/><path d="M17 6v5M17 29v5M3 20h5M26 20h5M7 10l4 4M23 26l4 4M27 10l-4 4M11 26l-4 4"/><circle cx="34" cy="10" r="4"/></svg>
      Installation
    </div>
    <div class="category">
      <svg width="44" height="40" viewBox="0 0 44 40" fill="none" stroke="#fff" stroke-width="2"><rect x="12" y="2" width="20" height="36" rx="2"/><rect x="18" y="10" width="8" height="12"/><path d="M18 16h8M18 30h8"/></svg>
      Safety Switches
    </div>
  </div>
</section>

<section class="services">
  <h2 class="section-title">OUR SERVICES</h2>
  <svg class="arrow" style="left:58px" width="12" height="22" viewBox="0 0 12 22"><path d="M10 2 2 11l8 9" stroke="#999" stroke-width="1.5" fill="none"/></svg>
  <svg class="arrow" style="left:1128px" width="12" height="22" viewBox="0 0 12 22"><path d="M2 2l8 9-8 9" stroke="#999" stroke-width="1.5" fill="none"/></svg>

  <article class="service-card" style="left:120px">
    <div class="photo" role="img" aria-label="Electrician fitting a chandelier in a home living room" style="background:linear-gradient(135deg,#c9a98a,#7d5d48 60%,#3c2e28)"></div>
    <h3>Domestic</h3><div class="rule"></div>
    <ul>
      <li>Mains</li><li>LED lighting</li>
      <li>Switchboards</li><li>Fans and ventilation</li>
      <li>Lighting installation</li><li>Safety Switches</li>
      <li style="grid-column:1/3">General Electrical wiring installations</li>
    </ul>
    <div class="btn btn-blue">READ MORE</div>
  </article>

  <article class="service-card" style="left:448px">
    <div class="photo" role="img" aria-label="Modern open-plan office fit out with lighting" style="background:linear-gradient(135deg,#d8dde0,#9aa3a8 55%,#4a4f52)"></div>
    <h3>Commercial</h3><div class="rule"></div>
    <ul class="single">
      <li>Complete Office Fit Outs</li>
      <li>Complete Retail &amp; Restaurant Fit Outs</li>
      <li>Energy Efficient Lighting</li>
      <li>Commercial Safety Switches</li>
    </ul>
    <div class="btn btn-red">READ MORE</div>
  </article>

  <article class="service-card" style="left:776px">
    <div class="photo" role="img" aria-label="Electrician working on an industrial switchboard" style="background:linear-gradient(135deg,#7d9ab8,#3f5f86 55%,#2a3548)"></div>
    <h3>Industrial</h3><div class="rule"></div>
    <ul class="single">
      <li>Three phase power</li>
      <li>Switchboard upgrades and installation</li>
      <li>Warehouse lighting</li>
      <li>Industrial safety switches</li>
    </ul>
    <div class="btn btn-blue">READ MORE</div>
  </article>
</section>

<section class="experience">
  <h2>WITH OVER 17 YEAR'S EXPERIENCE IN THE<br>ELECTRICAL INDUSTRY,</h2>
  <div class="photo" role="img" aria-label="Technician servicing a split system air conditioner" style="background:linear-gradient(135deg,#eef2f4,#c8d2d8 55%,#8a99a3)"></div>
  <div class="copy">
    <p>Tolvane Electrical provides a superior level of knowledge, a broad range of products and a high standard of customer service.</p>
    <p>To provide our customers with an immediate response within their timeframe, and deliver on-time, every time. Our friendly tradesmen are always professionally attired and treat your home or business with respect - we leave our jobs clean and tidy.</p>
  </div>
  <div class="outline-btn">DISCOVER ABOUT US</div>
</section>

<section class="why">
  <article class="why-card" style="left:120px">
    <div class="photo" role="img" aria-label="Technician installing an air conditioner while a customer watches" style="background:linear-gradient(135deg,#e8e6e2,#b9b4ad 55%,#6e6a66)"></div>
    <h3>WHY US?</h3><div class="rule"></div>
    <p>On Time We arrive on time. If there is an unavoidable delay we'll call ahead to let you know when we'll be there ...</p>
    <span class="more">READ MORE</span>
  </article>
  <article class="why-card" style="left:448px">
    <div class="photo" role="img" aria-label="Electrical tools and cables laid out on a bench" style="background:linear-gradient(135deg,#f0a040,#d85a3a 45%,#5a6a8a)"></div>
    <h3>QUALITY</h3><div class="rule"></div>
    <p>We are committed to best practice electrical safety standards and highest quality performance on the job ...</p>
    <span class="more hot">READ MORE</span>
  </article>
  <article class="why-card" style="left:776px">
    <div class="photo" role="img" aria-label="Tradesman with a tool belt in a workshop" style="background:linear-gradient(135deg,#c2a27e,#8a6a52 55%,#3e3530)"></div>
    <h3>PRICE</h3><div class="rule"></div>
    <p>Price is always important and our standard rates are competitive. Where jobs require an individual...</p>
    <span class="more">READ MORE</span>
  </article>
</section>

<section class="testimonials" role="img" aria-label="Dark background of light fittings and bulbs">
  <h2 class="section-title">TESTIMONIALS</h2>
  <blockquote><span class="q">“</span> Excellent service. Dalen came and quoted at the agreed time. The team showed up on time an completed on time. Dalen and his guys were friendly and professional and I would highly recommend them. I will look to them for any future work. <span class="q">”</span></blockquote>
  <div class="date">10 MAY 2019</div>
  <div class="name">Rhys K Marlow Heights, VIC</div>
  <div class="job">Split System Air Conditioning Verified Hired</div>
  <div class="dots"><i class="on"></i><i></i><i></i><i></i></div>
</section>

<section class="breakdown">
  <h2>24HR BREAKDOWN &amp; REPAIR SERVICE</h2>
  <p>Tolvane Electrical has a qualified electrician standing by with a fully stocked truck to assist you and your electrical needs around the clock. 24 hour emergency electrical services for your convenience.</p>
  <div class="btn btn-blue">CONTACT US</div>
</section>

<footer class="site-footer">
  <h4 style="left:240px">Get A Free Quotes</h4>
  <div class="field" style="left:240px;top:113px;width:167px;height:39px">Your Name</div>
  <div class="field" style="left:426px;top:113px;width:173px;height:39px">Email</div>
  <div class="field" style="left:240px;top:171px;width:167px;height:37px">Phone</div>
  <div class="field" style="left:426px;top:171px;width:173px;height:37px">Subject</div>
  <div class="field" style="left:240px;top:223px;width:359px;height:96px">Message ...</div>
  <div class="send">SEND MESSAGE</div>

  <h4 style="left:719px">Have any Questions?</h4>
  <div class="contact-info">
    <div class="tel">Call Us. 0417385926</div>
    <address>Tolvane Air and Electrical<br>Dalen Tolvane Westbrook<br>VIC 3999</address>
  </div>
  <div class="socials"><i></i><i></i><i></i><i></i></div>
  <div class="foot-rule"></div>
  <div class="copyright">© 2019 Tolvane Air and Electrical.<br>All Rights Reserved.</div>
</footer>

</body>
</html>
```